Website Performance Testing eBook for the software testing industry

Overview:
I would like an ebook/whitepaper designed. This ebook will be digital published on my website as a lead generation piece. The purpose is to give high level tips on what to look for and things to think about when working on a website performance testing project.
The ebook also demonstrates our expertise and knowledge on the topic.
Topic:
This is an ebook on software testing. Specifically, website performance testing.
About Veltrano:
Veltrano Solutions is an outsourcing development and software testing firm, and we provide expert services for application development, testing and data analytics. We extend our clients’ software testing capabilities with on-demand technical expertise. Our quality assurance resources work as part of our clients’ teams to help test applications on time and within budget.
Our model is designed to allocate the right mix of local and offshore resources in order to optimize expertise, speed and cost. We provide the ability to quickly add specialty skills to our client’s development team without them incurring long-term costs. The result is far better management of resource capacities and outcomes.
Background on our branding and previous pieces:
I have included a few of our previous ebooks and whitepapers. I like the look and feel of these pieces, however we have made updates to our brand guidelines since them, so the new brand guidelines will need to be incorporated, and I'd like to refresh/update what we have done in the past.
Refer to our website for an idea of our look and feel. This page is one of our newer sections and would be a good reference:
http://www.veltranosol.example/data-analytics/
Tone and feel:
- The look and feel should be professional, clean and polished.
- I like good use of whitespace.
- I would prefer to keep stock photography of people to a minimum. Any images should add to the content and be relevant to the content.
(Also, I uploaded some InDesign files in case you wanted to refer to those assets, but I didn't include the Links folder because they were too big. If there's anything you more you need, let me know)
Target Market(s)
Audience:
The audience is senior Quality Assurance and Software Testing professionals.
- 30-45 years old
- Technical mindset
- Interested in learning
Titles include
- QA Lead
- QA Manager
- QA Director
- Director or VP of Development
- QA Automation Engineer
Our customers are medium to large sized companies. Many are software companies, but many are also enterprises in all almost all industries.

```html
<!DOCTYPE html>
<html lang="en">
<head>
<meta charset="utf-8">
<title>The Do's and Don'ts of Website Performance Testing</title>
<link rel="stylesheet" href="https://fonts.googleapis.com/css2?family=Open+Sans:wght@300;400;700&display=swap">
<style>
  :root {
    --brand-red: #e13a33;
    --band-grey: #c4c7c7;
    --ink: #111111;
    --body: #4a4a4a;
    --muted: #6b6b6b;
    --icon-dark: #4b4c4e;
    --paper: #ffffff;
  }
  * { box-sizing: border-box; margin: 0; padding: 0; }
  html, body { width: 848px; height: 1200px; overflow: hidden; background: var(--paper); }
  .page {
    position: relative; width: 848px; height: 1200px; overflow: hidden;
    font-family: "Open Sans", sans-serif;
    background: linear-gradient(180deg, #f1f1f1 0, #ffffff 110px, #ffffff 1090px, #f1f1f1 1178px);
  }
  .band { position: absolute; left: 0; width: 848px; height: 21px; background: var(--band-grey); }
  .band::after { content: ""; position: absolute; top: 0; right: 0; width: 180px; height: 100%; background: var(--brand-red); }
  .band-top { top: 0; }
  .band-bottom { bottom: 0; }
  .brand {
    position: absolute; top: 42px; right: 14px;
    font-size: 24px; font-weight: 400; color: var(--brand-red); letter-spacing: 0.2px;
  }
  .title {
    position: absolute; left: 67px; top: 148px; width: 700px;
    font-size: 25.5px; font-weight: 700; line-height: 30px; color: var(--ink);
  }
  .intro {
    position: absolute; left: 67px; top: 232px; width: 704px;
    font-size: 19.8px; font-weight: 300; line-height: 24px; color: var(--body);
  }
  .tip { position: absolute; left: 80px; width: 690px; }
  .tip-icon { position: absolute; left: 1px; width: 51px; height: 51px; }
  .tip-text {
    position: absolute; left: 75px; width: 614px;
    font-size: 16.4px; font-weight: 300; line-height: 20.6px; color: var(--body);
    text-align: justify; hyphens: manual;
  }
  .footer { position: absolute; top: 1154px; font-size: 14px; font-weight: 300; color: var(--muted); }
  .breadcrumb { left: 58px; }
  .page-number { right: 25px; }
</style>
</head>
<body>
<div class="page">
  <div class="band band-top"></div>

  <div class="brand">Veltrano Solutions</div>

  <h1 class="title">THE DO’S AND DON’TS OF WEBSITE PERFORMANCE TESTING</h1>
  <p class="intro">When it is time to implement the test plan, avoid common strategic and tactical pitfalls:</p>

  <svg width="0" height="0" style="position:absolute">
    <defs>
      <symbol id="icon-do" viewBox="0 0 52 52">
        <circle cx="26" cy="26" r="26" fill="var(--icon-dark)"/>
        <path d="M18 27 l6 6 l11 -15" fill="none" stroke="#fff" stroke-width="2.4" stroke-linecap="round" stroke-linejoin="round"/>
      </symbol>
      <symbol id="icon-dont" viewBox="0 0 52 52">
        <circle cx="26" cy="26" r="26" fill="var(--brand-red)"/>
        <path d="M19.5 19.5 L32.5 32.5 M32.5 19.5 L19.5 32.5" stroke="#fff" stroke-width="3" stroke-linecap="round"/>
      </symbol>
    </defs>
  </svg>

  <div class="tip" style="top:315px">
    <svg class="tip-icon" style="top:14px"><use href="#icon-do"/></svg>
    <p class="tip-text">Do keep your in-house test infrastructure up-to-date even if you use cloud-based testing. It is your baseline environment for isolating cloud-based testing side-ef&shy;fects, which will drastically reduce the time for root cause analysis for many defects.</p>
  </div>

  <div class="tip" style="top:438px">
    <svg class="tip-icon" style="top:15px"><use href="#icon-do"/></svg>
    <p class="tip-text">Do use your live site, if one exists, to guide load and stress testing parameters on the developing site. For example, an initial test load might be the number of actual peak-hours orders multiplied by your expected growth rate plus 20 per&shy;cent overhead.</p>
  </div>

  <div class="tip" style="top:562px">
    <svg class="tip-icon" style="top:6px"><use href="#icon-do"/></svg>
    <p class="tip-text">Do track both client and server-side traffic during non-peak and peak perfor&shy;mance testing to determine ratios between traffic and processing activities, which often discovers imbalances.</p>
  </div>

  <div class="tip" style="top:664px">
    <svg class="tip-icon" style="top:-5px"><use href="#icon-do"/></svg>
    <p class="tip-text">Do test as many pages and combinations of page traversals as possible. Measure single page and page combination load times down to the component level.</p>
  </div>

  <div class="tip" style="top:746px">
    <svg class="tip-icon" style="top:11px"><use href="#icon-do"/></svg>
    <p class="tip-text">Do pay attention to which pages or activities are consuming an inordinate amount of time relative to other areas of the website. This helps optimize use of your test and repair resources.</p>
  </div>

  <div class="tip" style="top:849px">
    <svg class="tip-icon" style="top:-16px"><use href="#icon-do"/></svg>
    <p class="tip-text">Do distribute generated loads geographically and by network segment.</p>
  </div>

  <div class="tip" style="top:911px">
    <svg class="tip-icon" style="top:-5px"><use href="#icon-dont"/></svg>
    <p class="tip-text">Don’t ignore the dependency between page load times and user volume capacity. Measure both aspects at each stage of testing.</p>
  </div>

  <div class="tip" style="top:993px">
    <svg class="tip-icon" style="top:5px"><use href="#icon-dont"/></svg>
    <p class="tip-text">Don’t forget to process live web traffic logs to collect statistics on the types and volume of requests coming into your site so you can optimize load testing to reflect that reality.</p>
  </div>

  <div class="footer breadcrumb">Main Topic &nbsp;&gt; Main Subtopic &nbsp;&gt; Subtopic</div>
  <div class="footer page-number">Page 01 of 103</div>

  <div class="band band-bottom"></div>
</div>
</body>
</html>
```